Looking to overhaul my current Wordpress website

Current have a website www.quorvantek.com in wordpress, lack the skills or design flare to make it look and work better and more corporate professional.
We are a technology solution provider and software developer.
Updates
I think i have successfully uploaded my logo to assist with the wordpress theme and framework samples you will be providing.
Post me a message if you can locate it.
Target Market(s)
Small to business
Industry/Entity Type
Software
Font styles to use
Sans Serif
Requirements
Must have
- Must work on any device anywhere anytime, mobile ready in addition to traditional browser. Must be in work press for ongoing maintenance.
Nice to have
- use these website for a look and feel http://www.brightfallow.com.au/ http://www.halvorngroup.com/work http://www.halvorngroup.com/method
http://www.tallowquest.com/
Should not have
- No Flash!!,

```html
<!DOCTYPE html>
<html lang="en">
<head>
<meta charset="utf-8">
<title>About Us – Quorvantek</title>
<link href="https://fonts.googleapis.com/css2?family=Open+Sans:ital,wght@0,400;0,600;0,700;1,400&display=swap" rel="stylesheet">
<style>
:root{
  --ink:#3a3a3a;
  --body:#555;
  --muted:#999;
  --accent:#1a9cc4;
  --wood-a:#c9b39b;
  --wood-b:#dccbb6;
  --rule:#e6e6e6;
  --dark:#2b2b2b;
  --darker:#222;
  --footer-text:#bdbdbd;
  --footer-dim:#6f6f6f;
  --icon:#2a2a2a;
}
*{margin:0;padding:0;box-sizing:border-box}
html,body{width:832px;height:1200px;overflow:hidden;background:#fff}
body{position:relative;font-family:"Open Sans",Arial,sans-serif;color:var(--body)}
.abs{position:absolute}
.wood{background:linear-gradient(90deg,var(--wood-a),var(--wood-b) 30%,var(--wood-a) 55%,var(--wood-b) 80%,var(--wood-a))}
.topbar{left:0;top:0;width:832px;height:48px}
.call{left:23px;top:17px;width:145px;height:20px;background:#222;color:#fff;font-size:10px;font-weight:700;display:flex;align-items:center;gap:6px;padding-left:9px}
.social{top:17px;display:flex;gap:3px}
.social span{width:20px;height:20px;background:var(--icon);display:block}
.social .wide{width:72px;background:#2aa0c9}
.search{left:785px;top:17px;width:23px;height:20px;background:var(--icon)}
.header{left:0;top:48px;width:832px;height:91px;background:#fff}
.logo{left:40px;top:62px;display:flex;align-items:center;gap:10px}
.logo-mark{width:36px;height:36px;background:#2aa0c9}
.logo-name{font-size:30px;font-weight:700;color:#3c3c3c;letter-spacing:.5px}
.nav-bar{left:403px;top:48px;width:101px;height:3px;background:var(--accent)}
.nav{top:80px;font-size:12px;color:#444;letter-spacing:.2px}
.nav.active{color:var(--accent)}
.nav-sep{top:80px;width:1px;height:30px;background:#ececec}
.strip{left:0;top:139px;width:832px;height:51px}
.page-title{left:23px;top:206px;font-size:34px;font-weight:700;color:var(--ink);letter-spacing:-.5px}
.rule{left:0;width:832px;height:1px;background:var(--rule)}
.crumb{left:22px;top:273px;font-size:9.5px;color:#444;display:flex;gap:14px}
.crumb .lbl{color:var(--muted)}
.crumb .cur{color:var(--accent)}
.headline{left:19px;top:332px;width:780px;font-size:36px;line-height:40px;font-weight:600;color:var(--ink);letter-spacing:-.4px}
.hr{left:22px;top:452px;width:786px;height:1px;background:var(--rule)}
.h-section{font-size:11px;font-weight:700;color:#333}
.about{left:23px;top:494px;width:525px}
.about p{font-size:9.3px;line-height:15.2px;margin-top:15px;color:var(--body)}
.about p.tight{margin-top:0}
.testi{left:567px;top:494px;width:241px}
.dashes{display:flex;gap:3px;margin-top:8px}
.dashes i{display:block;width:14px;height:2px;background:#ccc}
.dashes i.on{background:#555}
.bubble{margin-top:16px;border:1px solid #e2e2e2;border-radius:5px;padding:16px 18px;font-size:8.6px;line-height:14.5px;font-style:italic;color:#555;position:relative;box-shadow:0 1px 3px rgba(0,0,0,.06)}
.bubble p+p{margin-top:8px}
.author{font-size:9px;color:#444;margin:14px 0 0 44px}
.footer-line{left:0;top:997px;width:832px;height:5px;background:#dde9ee}
.footer{left:0;top:1002px;width:832px;height:155px;background:var(--dark)}
.fcol{top:1013px;font-size:9.3px;color:var(--footer-text)}
.fcol h4{font-size:9.3px;font-weight:700;color:#eee;margin-bottom:28px}
.fcol .addr{line-height:15px}
.fcol ul{list-style:none}
.dim li{color:var(--footer-dim);font-size:10px;height:20px}
.dim li::before,.links li::before{content:"›";margin-right:8px;color:#666}
.links li{width:174px;border-bottom:1px solid #3a3a3a;height:27px;padding-top:7px;font-size:9px}
.links li.hl{color:var(--accent)}
.contacts h4{margin-bottom:14px}
.contacts div{line-height:14.5px}
.fsocial{display:flex;gap:4px;margin-top:10px}
.fsocial span{width:20px;height:20px;background:#3a3a3a;display:block}
.bottom{left:0;top:1157px;width:832px;height:43px;background:var(--darker)}
.copy{left:24px;top:1176px;font-size:10px;color:#8a8a8a;letter-spacing:.3px}
</style>
</head>
<body>
<div class="abs topbar wood" role="img" aria-label="Light timber plank background"></div>
<div class="abs call">
  <svg width="9" height="11" viewBox="0 0 9 11"><path d="M2 0 L4 3 L3 4 Q4 7 6 8 L7 7 L9 9 L7 11 Q0 9 0 2 Z" fill="#fff"/></svg>
  Call Us : 08 5550 1427
</div>
<div class="abs social" style="left:604px"><span></span><span></span><span class="wide"></span><span></span><span></span></div>
<div class="abs search"><svg width="23" height="20" viewBox="0 0 23 20"><circle cx="12.5" cy="9" r="3" fill="none" stroke="#fff" stroke-width="1.6"/><line x1="10.3" y1="11.2" x2="8" y2="13.5" stroke="#fff" stroke-width="1.8"/></svg></div>

<header class="abs header"></header>
<div class="abs logo"><span class="logo-mark"></span><span class="logo-name">Quorvantek</span></div>
<div class="abs nav-bar"></div>
<div class="abs nav-sep" style="left:318px"></div>
<div class="abs nav active" style="left:345px">HOME</div>
<div class="abs nav-sep" style="left:404px"></div>
<div class="abs nav" style="left:420px">ABOUT US &#9662;</div>
<div class="abs nav-sep" style="left:503px"></div>
<div class="abs nav" style="left:514px">OUR SERVICES &#9662;</div>
<div class="abs nav-sep" style="left:621px"></div>
<div class="abs nav" style="left:632px">OUR SOLUTIONS</div>
<div class="abs nav-sep" style="left:741px"></div>
<div class="abs nav" style="left:756px">CONTACTS</div>

<div class="abs strip wood" role="img" aria-label="Light timber plank banner"></div>

<h1 class="abs page-title">About Us.</h1>
<div class="abs rule" style="top:260px"></div>
<div class="abs crumb"><span class="lbl">You are here:</span><span>Home</span><span class="cur">About</span></div>
<div class="abs rule" style="top:294px"></div>

<h2 class="abs headline">Create your own visual style... let it be unique for yourself and yet identifiable for others.</h2>
<div class="abs hr"></div>

<section class="abs about">
  <h3 class="h-section">ABOUT QUORVANTEK</h3>
  <p>Quorvantek was founded in 2007 with the mission to become the go-to technology consultancy for building world-class, one of a kind, web applications and web based businesses.</p>
  <p>We have seen many great ideas killed because of poor execution by technology teams that didn't treat their work as craft.</p>
  <p class="tight">We knew we could provide the perfect place for entrepreneurs to come for founder level design and engineering leadership, and where large companies could inject entrepreneurial innovation into their existing product development efforts.</p>
  <p>Our team of engineers, product management, user experience and design talent is our dream-team of talent we will use on our own products, such as Fernline CRM, and also the same team our clients have access to.</p>
  <p>By having the best people we're able to do a few things: attract more great people, retain our great people, build applications faster by being smarter and be able to have the right team in place for when we build applications for ourselves.</p>
  <p>In a company like Quorvantek, engineering and creativity drives the business. Our people are all a aligned to creating well architected, extensible, highly scalable applications.</p>
  <p>We don't do ad-hoc, throw-away development ( not to confuse that with throw-away technology used in the customer development process ).</p>
</section>

<aside class="abs testi">
  <h3 class="h-section">CLIENTS TESTIMONIALS</h3>
  <div class="dashes"><i></i><i class="on"></i><i></i><i></i></div>
  <div class="bubble">
    <p>“” Ectetur adipiscing elit. Aenean nisl orci, cond imeat eucons. Lorem ipsum doit amet, cons ecteorem ipsum dolor sit amet, ectetur.</p>
    <p>Lorem ipsum doit amet, cons ecteorem ipsum dolor sit amet, ectetur adipiscing elit. ”</p>
  </div>
  <div class="author">JONH DOE</div>
</aside>

<div class="abs footer-line"></div>
<footer class="abs footer"></footer>
<div class="abs fcol" style="left:21px">
  <h4>ABOUT QUORVANTEK.</h4>
  <div class="addr">Tallowquest, Inc.<br>48 Larkspur Ave<br>Suite 120<br>Fenwick MA 01999</div>
</div>
<div class="abs fcol" style="left:221px">
  <h4 style="margin-bottom:20px">ABOUT US</h4>
  <ul class="dim"><li>Our team</li><li>Background</li><li>Datacenter features</li><li>Tell us about your project</li></ul>
</div>
<div class="abs fcol" style="left:428px">
  <h4 style="margin-bottom:12px">USEFUL STUFF</h4>
  <ul class="links"><li>Lorem ipsum dolor sit amet</li><li>Consectetur adipiscing</li><li class="hl">Aenean nisl orcirtymentum</li><li>Consequat eu</li></ul>
</div>
<div class="abs fcol contacts" style="left:652px;top:1008px">
  <h4>Contacts</h4>
  <div>Phone: 08 5550 1427</div>
  <div>Email: sales@quorvantek.com.au</div>
  <div>Web: www.quorvantek.com</div>
  <div class="fsocial"><span></span><span></span><span></span><span></span></div>
</div>
<div class="abs bottom"></div>
<div class="abs copy">Copyright © 2013 QUORVANTEK</div>
</body>
</html>
```